website for local kavenda practicioner and yoga teacher trainer

The website should function primarily as:
A place where people can discover Kavenda and book sessions.
A central hub connecting all of my work.
A professional home that reflects my personality and approach.
Website design for Liesbet Oonwerk — Kavenda® Structural Integration practitioner, movement educator, yoga teacher and teacher trainer.
A website that can grow with future projects.
The website should feel: Warm, Human, Invitational, Professional, Accessible, Intelligent, Calm, Clear, Playful, Exploratory, Trustworthy
Avoid: New age aesthetics, Mystical clichés, Excessive spirituality, ”Guru" vibes, Overly clinical design, Corporate wellness branding, Busy layouts
Think: modern, grounded, curious and real.
My work combines three interconnected areas:
1.Bodywork: Touch, structure, awareness and one-on-one support.
2. Movement: Yoga, Pilates and embodied movement.
3. Education: Teacher trainings, workshops and continued learning.
Underlying values:
Curiosity over certainty
Possibility over perfection
Complexity without overwhelm
Science and lived experience together
Exploration rather than dogma
Human beings before methods
The primary goal of the website is to introduce people to Kavenda® Structural Integration and make it easy for them to:
Understand what Kavenda is
Discover whether it might be relevant for them
Learn what to expect from a session
Book an appointment
Booking should always feel visible and easy.
Secondary Goal: Present all other aspects of my work in one coherent place:
Yoga classes
Pilates classes
Teacher trainings
Workshops
Retreats
One-on-one movement sessions
Collaborations with studios
Website Structure
1: HOME
1.1.Hero Section: Large welcoming image
1.2 Two Main Pathways
- Bodywork: Kavenda® Structural Integration
- Movement & Education: Yoga, Pilates, trainings, workshops and retreats
- About Preview: Small introduction with portrait. + Button:
Read More
1.3 Current Events / What's Coming Up: Upcoming trainings, workshops and retreats. (This section should be easy to update)
1.4. Contact / Newsletter: Simple contact information
2: Kavenda® Structural Integration
What is Kavenda?
For whom is it?
What does a session look like?
FAQ
Prices
Booking
Future possibility:
Kaven Movement sessions
3: Movement
- Introductory text.
- Studio Classes (link to “my home base” - > local yoga studio)
- One-to-One Sessions: booking option (this is small; not a key aspect I want to promote)
- Workshops/ Retreats / Teacher Trainings => This section should be flexible and easy to update. Visitors should be able to click into specific offerings.
4. Events
Dynamic page for: Teacher trainings, Retreats, Workshops (see section in movement; here more elaborate)
Each event should contain: Image, Short description, Location, Date, Button for more information. (Linking to hosting studio/location)
5. Work With Me
For studios, organisations and teacher training schools.
Examples: Guest teaching, Workshops, Anatomy, Sequencing, Teacher development , Continuing education -> Clear call-to-action.
Call to action!!=> Book a Session
Prominent button in the navigation.
Footer:
- About Me: Longer biography (6th page)
Personal story and background.
- Testimonials (7th page): Separate page containing testimonials from:
Kavenda clients
Students
Teacher trainees
- Contact: 8th page
Visual Direction
Natural textures. Lots of white space.Editorial feeling.Professional photography.Simple navigation.
Less "wellness influencer.” More:Thoughtful, Contemporary, Timeless, Grounded, Human
Photography should show:
Teaching
Hands-on work
Natural movement
Real interaction
Simplicity
Avoid stereotypical yoga imagery and overly spiritual aesthetics.
Keywords
Warm. Curious. Human. Professional. Embodied. Intelligent. Accessible. Playful. Grounded. Exploratory. Real.
Inspiration / Core Message
Helping people feel more at home in their bodies through touch, movement and education.
The website should communicate that these are not separate services, but different expressions of the same intention:
Bodywork • Movement • Education.
Colours:
light orange/beige: e3d5c4
light orange/off white: f9f7f3
gray azure: 556b78
orange: d07b5a
grey orange: c09f80
dark grey: 3e3e3e
dark gray cyan 2f4f4f
gray green colour: a7c4a0
Fonts: Montserrat and Poppins + raleway
In added documents a try out idea of a website + logo. I will mainly use the logo with diffrent colours (image next to text).
My audience consists of people who want to feel more at home in their bodies and who appreciate a thoughtful, grounded and human approach to movement, touch and education. (30-65yo)
wellbeing
5+ page
- montserrat, poppins, raleway

```html
<!DOCTYPE html>
<html lang="en">
<head>
<meta charset="utf-8">
<title>Liesbet Oonwerk — Bodywork, Movement, Education</title>
<link href="https://fonts.googleapis.com/css2?family=Montserrat:wght@400;500;600;700&family=Poppins:wght@300;400;500;600&family=Raleway:wght@400;500&display=swap" rel="stylesheet">
<style>
:root{
  --beige:#e3d5c4; --offwhite:#f9f7f3; --azure:#556b78; --orange:#d07b5a;
  --greyorange:#c09f80; --panel:#c8a886; --dark:#3e3e3e; --cyan:#2f4f4f;
  --sage:#a7c4a0; --olive:#4f5a34; --ink:#333; --frame:#8c8c8c;
}
*{box-sizing:border-box;margin:0;padding:0}
html,body{width:1200px;height:3160px;overflow:hidden}
body{background:var(--frame);font-family:'Poppins',sans-serif;color:var(--ink)}
.page{position:absolute;left:81px;top:81px;width:1038px;height:2999px;background:#fff;overflow:hidden}
.abs{position:absolute}
.deco-word{position:absolute;font-family:'Montserrat',sans-serif;font-weight:500;color:#f3e9e2;letter-spacing:8px;white-space:nowrap;transform-origin:left top}
/* nav */
.nav{left:15px;top:16px;width:1010px;height:44px;z-index:5}
.brand{left:0;top:6px;display:flex;align-items:center;gap:7px;white-space:nowrap}
.brand-dot{width:26px;height:26px;border-radius:50%;background:var(--orange);flex:none}
.brand-name{font-family:'Raleway',sans-serif;font-size:16px;font-weight:500;color:var(--azure)}
.nav-links{left:198px;top:14px;display:flex;gap:16px;font-size:10px;color:#333;white-space:nowrap}
.nav-cta{left:695px;top:6px;background:var(--azure);color:#fff;font-size:10px;padding:8px 11px;border-radius:14px;white-space:nowrap}
/* hero */
.kicker{left:64px;top:134px;font-family:'Montserrat',sans-serif;font-weight:600;font-size:32px;letter-spacing:18px;color:var(--orange)}
.hero-title{left:64px;top:172px;font-family:'Montserrat',sans-serif;font-weight:700;font-size:52px;line-height:65px;color:var(--azure);white-space:nowrap}
.hero-title span{color:var(--orange)}
.hero-wave{left:62px;top:310px}
.hero-text{left:64px;top:334px;width:560px;font-size:19px;line-height:27px;color:#333}
.btn{position:absolute;font-family:'Montserrat',sans-serif;font-weight:500;letter-spacing:.5px}
.btn-solid{left:64px;top:434px;width:176px;height:38px;background:var(--orange);color:#fff;font-size:17px;text-align:center;line-height:38px}
.btn-line{left:249px;top:434px;width:200px;height:38px;border:1.5px solid var(--orange);color:var(--orange);font-size:17px;text-align:center;line-height:35px}
.hero-art{left:600px;top:0;z-index:1}
/* cards */
.card{position:absolute;top:618px;width:284px;height:338px;background:#fff;box-shadow:0 2px 8px rgba(0,0,0,.12)}
.card-photo{height:166px}
.card-icon{position:absolute;left:24px;top:132px;width:60px;height:60px;border-radius:50%;background:#fff;box-shadow:0 1px 5px rgba(0,0,0,.15);display:flex;align-items:center;justify-content:center}
.card-body{position:absolute;left:26px;top:204px;width:240px}
.card h3{font-family:'Montserrat',sans-serif;font-weight:600;font-size:22px}
.card h4{font-size:10px;font-weight:600;margin:4px 0 12px}
.card p{font-size:9.5px;line-height:14.5px;color:#444}
.card .more{display:block;margin-top:12px;font-size:9.5px;letter-spacing:.5px;text-decoration:underline}
.c-orange{color:var(--orange)} .c-azure{color:var(--azure)} .c-gold{color:#c9915f}
/* kavenda */
.kv-photo{left:66px;top:1023px;width:452px;height:378px}
.kv-panel{left:518px;top:1023px;width:454px;height:378px;background:var(--panel);color:#fff;padding:44px 42px 0 46px}
.kv-panel h2{font-family:'Montserrat',sans-serif;font-weight:500;font-size:29px;line-height:36px}
.kv-panel .lead{font-size:9.5px;line-height:15px;margin-top:10px;opacity:.95}
.kv-benefits{display:flex;gap:22px;margin-top:14px}
.kv-benefit{width:84px;font-size:9.5px;line-height:11px;text-align:center}
.kv-benefit svg{display:block;margin:0 auto 6px}
.kv-benefit:first-child{text-align:left;width:58px}
.kv-benefit:first-child svg{margin-left:4px}
.faq{margin-top:12px;border-top:1px solid rgba(255,255,255,.7)}
.faq div{display:flex;justify-content:space-between;font-size:9.5px;padding:5px 0 4px;border-bottom:1px solid rgba(255,255,255,.35)}
.kv-btn{display:inline-block;margin-top:12px;background:#fff;color:var(--azure);font-size:9.5px;font-weight:500;padding:4px 8px}
/* about */
.about{left:0;top:1382px;width:1038px;height:394px;background:var(--olive)}
.about-photo{left:440px;top:0;width:598px;height:394px}
.about-kicker{left:64px;top:74px;font-family:'Montserrat',sans-serif;font-weight:500;font-size:15px;color:var(--orange)}
.about h2{position:absolute;left:64px;top:94px;font-family:'Montserrat',sans-serif;font-weight:500;font-size:30px;line-height:34px;color:#fff}
.about-text{left:64px;top:174px;width:480px;font-size:10px;line-height:15px;color:#fff}
.about-btn{left:64px;top:224px;background:var(--azure);color:#fff;font-size:9.5px;font-weight:500;padding:4px 8px}
.values{left:64px;top:280px;display:flex;gap:22px}
.value{width:82px;text-align:center;font-size:9.5px;line-height:12px;color:#fff}
.value svg{display:block;margin:0 auto 6px}
.quote-box{left:504px;top:232px;width:124px;height:104px;background:var(--orange);border-radius:6px;color:#fff;padding:16px 16px;font-size:13px;line-height:18px}
.quote-box small{display:block;font-size:9.5px;margin-top:4px}
/* events */
.sec-title{position:absolute;font-family:'Montserrat',sans-serif;font-weight:500;font-size:30px;color:var(--dark)}
.view-all{left:820px;top:1843px;font-size:11px;color:var(--azure);letter-spacing:.5px;text-decoration:underline;display:flex;align-items:center;gap:18px}
.event{position:absolute;top:1890px;width:218px;height:117px;background:#fff;box-shadow:0 1px 5px rgba(0,0,0,.12)}
.event-photo{position:absolute;left:0;top:0;width:94px;height:117px}
.event-body{position:absolute;left:107px;top:10px;width:106px}
.event .tag{font-size:9px;color:var(--orange);letter-spacing:.3px}
.event h4{font-family:'Montserrat',sans-serif;font-weight:700;font-size:10.5px;line-height:12px;color:#333;margin:3px 0 8px}
.event p{font-size:9.5px;line-height:12px;color:#444}
.event .details{display:block;margin-top:6px;font-size:9.5px;color:var(--azure)}
/* work with me */
.wwm{left:64px;top:2036px;width:910px;height:151px;background:var(--azure);color:#fff}
.wwm h2{position:absolute;left:30px;top:24px;font-family:'Montserrat',sans-serif;font-weight:500;font-size:32px}
.wwm p{position:absolute;left:30px;top:68px;width:290px;font-size:9.5px;line-height:13px}
.wwm .btn-mini{position:absolute;left:30px;top:102px;background:var(--orange);font-size:9.5px;padding:4px 10px;font-weight:500}
.wwm-items{position:absolute;left:326px;top:38px;display:flex}
.wwm-item{width:146px;height:84px;border-left:1px solid rgba(255,255,255,.3);text-align:center;font-size:9.5px;line-height:12px;padding-top:6px}
.wwm-item svg{display:block;margin:0 auto 12px}
/* testimonials */
.testi{position:absolute;top:2250px;width:292px;height:118px;background:#fff;box-shadow:0 1px 5px rgba(0,0,0,.1);padding:26px 28px;font-size:9.5px;line-height:14px;color:#333}
.testi span{display:block;margin-top:10px}
.dots{left:481px;top:2384px;display:flex;gap:8px}
.dots i{width:7px;height:7px;border-radius:50%;background:#ddd}
.dots i.on{background:#888}
/* cta */
.cta{left:0;top:2431px;width:1038px;height:271px}
.cta h2{position:absolute;left:64px;top:60px;font-family:'Montserrat',sans-serif;font-weight:500;font-size:31px;line-height:39px;color:#fff}
.cta p{position:absolute;left:64px;top:142px;font-family:'Montserrat',sans-serif;font-size:19px;color:#fff}
.cta .btn-cta{position:absolute;left:64px;top:184px;background:var(--azure);color:#fff;font-family:'Montserrat',sans-serif;font-size:13px;font-weight:500;padding:7px 10px}
/* newsletter */
.news{left:0;top:2702px;width:1038px;height:82px;background:var(--orange);color:#fff}
.news h3{position:absolute;left:122px;top:22px;font-family:'Montserrat',sans-serif;font-weight:500;font-size:22px}
.news p{position:absolute;left:122px;top:50px;font-size:9.5px}
.news .input{position:absolute;left:466px;top:24px;width:200px;height:34px;background:#fff;color:#333;font-size:10px;padding:11px 14px}
.news .sub{position:absolute;left:671px;top:24px;width:91px;height:34px;background:var(--azure);font-size:9.5px;font-weight:600;text-align:center;line-height:34px}
.socials{position:absolute;left:825px;top:27px;display:flex;gap:10px}
.socials i{width:30px;height:30px;border-radius:50%;border:1.5px solid #fff}
/* footer */
.footer{left:0;top:2784px;width:1038px;height:215px;background:var(--dark);color:#fff}
.f-brand{position:absolute;left:64px;top:44px;display:flex;align-items:center;gap:8px;white-space:nowrap}
.f-brand .brand-dot{width:30px;height:30px}
.f-brand span{font-family:'Raleway',sans-serif;font-size:19px;font-weight:500}
.f-about{position:absolute;left:64px;top:92px;width:180px;font-size:9.5px;line-height:14px}
.f-col{position:absolute;top:36px;font-size:9.5px;line-height:15px}
.f-col h5{font-family:'Montserrat',sans-serif;font-weight:500;font-size:16px;color:var(--orange);margin-bottom:6px}
.f-col li{list-style:none}
.f-col li::before{content:"▸ ";color:var(--orange)}
.f-contact{display:flex;gap:8px;align-items:center;margin-bottom:10px}
.f-contact .ico{width:24px;height:24px;border-radius:50%;border:1.5px solid var(--orange);display:flex;align-items:center;justify-content:center}
.f-contact small{display:block;color:var(--orange);font-size:8.5px;line-height:10px}
.f-quote{position:absolute;left:854px;top:36px;font-family:'Raleway',sans-serif;font-size:18px;line-height:25px}
.f-quote small{display:block;font-size:11px;color:var(--orange);font-family:'Poppins',sans-serif}
.f-legal{position:absolute;left:0;top:178px;width:1038px;text-align:center;font-size:9.5px}
</style>
</head>
<body>
<main class="page">

  <div class="deco-word" style="left:38px;top:170px;font-size:80px;transform:rotate(90deg) translateY(-80px);" aria-hidden="true">LIESBET</div>
  <div class="deco-word" style="left:122px;top:1130px;font-size:80px;transform:rotate(90deg) translateY(-80px);color:#f8efea" aria-hidden="true">YOGA</div>
  <div class="deco-word" style="left:1038px;top:620px;font-size:80px;transform:rotate(90deg);" aria-hidden="true">OONWERK</div>
  <div class="deco-word" style="left:1038px;top:1780px;font-size:80px;transform:rotate(90deg);color:#f8efea" aria-hidden="true">BODYWORK</div>

  <!-- hero artwork -->
  <svg class="abs hero-art" width="438" height="560" viewBox="0 0 438 560" role="img" aria-label="Teacher guiding a student into a low lunge on a yoga mat in a bright studio">
    <defs><linearGradient id="heroFill" x1="0" y1="0" x2="0" y2="1"><stop offset="0" stop-color="#ece8e2"/><stop offset=".6" stop-color="#b9aea4"/><stop offset="1" stop-color="#4a4a50"/></linearGradient></defs>
    <path d="M250 60 C 200 110 250 160 210 220 C 170 280 220 340 180 390 C 150 430 190 470 240 470 L 438 470 L 438 60 Z" fill="#f5ede6"/>
    <path d="M340 90 C 300 120 230 140 200 200 C 170 260 90 280 60 330 C 30 380 60 420 80 450 C 120 520 220 560 300 540 C 380 520 430 470 438 420 L 438 110 C 400 130 370 120 340 90 Z" fill="url(#heroFill)"/>
  </svg>

  <!-- navigation -->
  <nav class="abs nav">
    <div class="abs brand"><span class="brand-dot"></span><span class="brand-name">Liesbet Oonwerk</span></div>
    <div class="abs nav-links"><span>Home</span><span>Kavenda®</span><span>Movement</span><span>Events</span><span>Work With Me</span><span>About</span><span>Testimonials</span><span>Contact</span></div>
    <div class="abs nav-cta">Book a Session</div>
  </nav>

  <!-- hero -->
  <div class="abs kicker">HELPING</div>
  <h1 class="abs hero-title">People Feel More at<br>Home in Their <span>Bodies</span></h1>
  <svg class="abs hero-wave" width="364" height="14" viewBox="0 0 364 14" aria-hidden="true"><path d="M2 7 Q 20 1 38 7 T 74 7 T 110 7 T 146 7 T 182 7 T 218 7 T 254 7 T 290 7 T 326 7 T 362 7" fill="none" stroke="var(--azure)" stroke-width="3" stroke-linecap="round"/></svg>
  <p class="abs hero-text">Kavenda® Structural Integration, movement and education for a body that moves, adapts and lives with more freedom.</p>
  <div class="btn btn-solid">BOOK A SESSION</div>
  <div class="btn btn-line">DISCOVER KAVENDA</div>

  <!-- pathways -->
  <article class="card" style="left:64px">
    <div class="card-photo" role="img" aria-label="Hands-on bodywork on a client's back" style="background:linear-gradient(135deg,#7a4a30,#c99870 55%,#5b3a2a)"></div>
    <div class="card-icon"><svg width="30" height="30" viewBox="0 0 30 30" fill="none" stroke="var(--orange)" stroke-width="1.4"><circle cx="15" cy="7" r="3"/><path d="M15 11v9M11 14l4 2 4-2M9 22c2 4 10 4 12 0"/></svg></div>
    <div class="card-body">
      <h3 class="c-orange">BODYWORK</h3>
      <h4>Kavenda® Structural Integration</h4>
      <p>One-on-one sessions that look at how your body is organised. More ease, more balance, more you.</p>
      <span class="more c-orange">LEARN MORE →</span>
    </div>
  </article>
  <article class="card" style="left:377px">
    <div class="card-photo" role="img" aria-label="Woman in a low lunge with arm raised in a sunlit studio" style="background:linear-gradient(135deg,#e6d2b8,#c9a47a 60%,#8b6a4a)"></div>
    <div class="card-icon"><svg width="30" height="30" viewBox="0 0 30 30" fill="none" stroke="var(--azure)" stroke-width="1.4"><circle cx="13" cy="6" r="3"/><path d="M13 10l-2 8 5 4v5M11 18l-5 7M13 11l8-4"/></svg></div>
    <div class="card-body">
      <h3 class="c-azure">MOVEMENT</h3>
      <h4>Yoga &amp; Pilates</h4>
      <p>Classes and one-to-one sessions that built strength, awareness and possibility.</p>
      <span class="more c-azure">EXPLORE MOVEMENT →</span>
    </div>
  </article>
  <article class="card" style="left:690px">
    <div class="card-photo" role="img" aria-label="Small group of students sitting together on the floor in a workshop" style="background:linear-gradient(135deg,#d8c8b4,#9c8a78 55%,#5d5148)"></div>
    <div class="card-icon"><svg width="30" height="30" viewBox="0 0 30 30" fill="none" stroke="#c9915f" stroke-width="1.4"><path d="M4 10h10v14H4zM16 10h10v14H16z"/><circle cx="15" cy="5" r="3"/></svg></div>
    <div class="card-body">
      <h3 class="c-gold">EDUCATION</h3>
      <h4>Trainings, Workshops &amp; Retreats</h4>
      <p>Inspiring learning experiences for teachers and movers who want to go deeper.</p>
      <span class="more c-gold">VIEW EVENTS →</span>
    </div>
  </article>

  <!-- kavenda intro -->
  <div class="abs kv-photo" role="img" aria-label="Practitioner working on a client lying on a treatment table in warm light" style="background:linear-gradient(120deg,#6b4530,#b8875e 45%,#e1c7a3)"></div>
  <section class="abs kv-panel">
    <h2>What is Kavenda®<br>Structural Integration?</h2>
    <p class="lead">Kavenda helps your body function with more ease and efficiency by working with the underlying structure.</p>
    <div class="kv-benefits">
      <div class="kv-benefit"><svg width="26" height="26" viewBox="0 0 26 26" fill="none" stroke="#fff" stroke-width="1.3"><circle cx="13" cy="13" r="10"/><path d="M8 13l4 4 7-8"/></svg>More ease &amp; balance</div>
      <div class="kv-benefit"><svg width="26" height="26" viewBox="0 0 26 26" fill="none" stroke="#fff" stroke-width="1.3"><circle cx="13" cy="5" r="3"/><path d="M13 8v12M8 12h10M9 24l4-4 4 4"/></svg>Improved posture &amp; movement</div>
      <div class="kv-benefit"><svg width="26" height="26" viewBox="0 0 26 26" fill="none" stroke="#fff" stroke-width="1.3"><circle cx="13" cy="5" r="3"/><path d="M5 10l8 2 8-2M13 12v6l-4 6M13 18l4 6"/></svg>Less pain, more freedom</div>
      <div class="kv-benefit"><svg width="26" height="26" viewBox="0 0 26 26" fill="none" stroke="#fff" stroke-width="1.3"><circle cx="13" cy="9" r="3"/><path d="M13 12v10M6 8l-3-2M20 8l3-2M13 2v2"/></svg>Greater body awareness</div>
    </div>
    <div class="faq">
      <div><span>What happens in a session?</span><span>+</span></div>
      <div><span>Who is Kavenda for?</span><span>+</span></div>
      <div><span>How many sessions will I need?</span><span>+</span></div>
    </div>
    <span class="kv-btn">LEARN MORE ABOUT KAVENDA</span>
  </section>

  <!-- about preview -->
  <section class="abs about">
    <div class="abs about-photo" role="img" aria-label="Portrait of the practitioner sitting outdoors in tall grass" style="background:linear-gradient(90deg,var(--olive) 0%,#6b7444 25%,#8f9660 60%,#6d7048 100%)"></div>
    <div class="abs about-kicker">HI, I'M LIESBET</div>
    <h2>Movement is how I explore,<br>connect and make sense of life.</h2>
    <p class="abs about-text">I bring together bodywork, movement and education to support people in feeling more at home in their bodies. Curious by nature, I love complex things and simple truths. I work in Leiden and internationally, in English, Dutch and French.</p>
    <span class="abs about-btn">READ MY STORY</span>
    <div class="abs values">
      <div class="value"><svg width="28" height="28" viewBox="0 0 28 28" fill="none" stroke="var(--orange)" stroke-width="1.3"><circle cx="14" cy="11" r="7"/><path d="M11 20h6M12 24h4"/></svg>Curiosity over certainty</div>
      <div class="value"><svg width="28" height="28" viewBox="0 0 28 28" fill="none" stroke="var(--orange)" stroke-width="1.3"><circle cx="14" cy="8" r="4"/><path d="M6 24c0-6 4-10 8-10s8 4 8 10"/></svg>Possibility over perfection</div>
      <div class="value"><svg width="28" height="28" viewBox="0 0 28 28" fill="none" stroke="var(--orange)" stroke-width="1.3"><circle cx="14" cy="14" r="10"/><circle cx="14" cy="11" r="3"/><path d="M9 21c1-4 9-4 10 0"/></svg>Science &amp; lived experience</div>
      <div class="value"><svg width="28" height="28" viewBox="0 0 28 28" fill="none" stroke="var(--orange)" stroke-width="1.3"><path d="M4 24l8-10 5 5 7-12"/><circle cx="20" cy="5" r="2"/></svg>Exploration over dogma</div>
    </div>
    <div class="abs quote-box">“Bodies are plastic to the intent of life.”<small>— Ilse Varen</small></div>
  </section>

  <!-- events -->
  <h2 class="sec-title" style="left:64px;top:1833px">WHAT'S COMING UP</h2>
  <div class="abs view-all"><span>VIEW ALL EVENTS</span><svg width="20" height="8" viewBox="0 0 20 8" fill="none" stroke="var(--azure)" stroke-width="1.2"><path d="M0 4h19M15 1l4 3-4 3"/></svg></div>
  <article class="event" style="left:64px"><div class="event-photo" role="img" aria-label="Woman stretching on a mat in a studio" style="background:linear-gradient(160deg,#e8dccb,#a88a6a)"></div><div class="event-body"><div class="tag">TRAINING</div><h4>Kaven Movement™ Intro Training</h4><p>12–14 July 2025<br>Leiden, NL</p><span class="details">VIEW DETAILS →</span></div></article>
  <article class="event" style="left:294px"><div class="event-photo" role="img" aria-label="Woman in a seated forward fold by the sea" style="background:linear-gradient(160deg,#9fb3c0,#c8b49a)"></div><div class="event-body"><div class="tag">WORKSHOP</div><h4>Breath, Touch &amp; Fascia</h4><p>20 September 2025<br>Amsterdam, NL</p><span class="details">VIEW DETAILS →</span></div></article>
  <article class="event" style="left:526px"><div class="event-photo" role="img" aria-label="Woman in a standing pose on a green hillside" style="background:linear-gradient(160deg,#a9b88e,#5e6d44)"></div><div class="event-body"><div class="tag">RETREAT</div><h4>Embodied Awareness Retreat</h4><p>6–12 October 2025<br>Portugal</p><span class="details">VIEW DETAILS →</span></div></article>
  <article class="event" style="left:757px"><div class="event-photo" role="img" aria-label="Woman sitting cross-legged on a mat" style="background:linear-gradient(160deg,#d6c7b4,#7a6a5a)"></div><div class="event-body"><div class="tag">TRAINING</div><h4>Yoga Teacher Training 200HR</h4><p>Jan–May 2026<br>Leiden, NL</p><span class="details">VIEW DETAILS →</span></div></article>

  <!-- work with me -->
  <section class="abs wwm">
    <h2>WORK WITH ME</h2>
    <p>For studios, organisations and teacher training schools. Let's create something meaningful together.</p>
    <span class="btn-mini">LET'S CONNECT</span>
    <div class="wwm-items">
      <div class="wwm-item"><svg width="30" height="30" viewBox="0 0 30 30" fill="none" stroke="#e39a7b" stroke-width="1.3"><rect x="3" y="3" width="24" height="14"/><circle cx="9" cy="22" r="3"/><circle cx="21" cy="22" r="3"/></svg>Guest Teaching<br>&amp; Workshops</div>
      <div class="wwm-item"><svg width="30" height="30" viewBox="0 0 30 30" fill="none" stroke="#e39a7b" stroke-width="1.3"><path d="M4 8h22v18H4z"/><circle cx="15" cy="15" r="4"/><path d="M11 4h8"/></svg>Anatomy &amp;<br>Education</div>
      <div class="wwm-item"><svg width="30" height="30" viewBox="0 0 30 30" fill="none" stroke="#e39a7b" stroke-width="1.3"><circle cx="15" cy="12" r="7"/><path d="M15 2v3M5 12H2M28 12h-3M8 26h14"/></svg>Teacher Development<br>&amp; Mentoring</div>
      <div class="wwm-item"><svg width="30" height="30" viewBox="0 0 30 30" fill="none" stroke="#e39a7b" stroke-width="1.3"><rect x="4" y="4" width="22" height="16"/><path d="M10 26h10M15 20v6M9 12l4 3 7-6"/></svg>Trainings &amp;<br>Continuing Ed.</div>
    </div>
  </section>

  <!-- testimonials -->
  <h2 class="sec-title" style="left:0;width:1038px;text-align:center;top:2220px">WHAT'S COMING UP</h2>
  <blockquote class="testi" style="left:64px">"Kavenda with Liesbet was truly transformative. I feel taller, lighter and more connected to myself."<span>— Client, Leiden</span></blockquote>
  <blockquote class="testi" style="left:373px">"Kavenda with Liesbet was truly transformative. I feel taller, lighter and more connected to myself."<span>— Client, Leiden</span></blockquote>
  <blockquote class="testi" style="left:682px">"Kavenda with Liesbet was truly transformative. I feel taller, lighter and more connected to myself."<span>— Client, Leiden</span></blockquote>
  <div class="abs dots"><i></i><i></i><i></i><i class="on"></i><i></i><i></i><i></i></div>

  <!-- call to action -->
  <section class="abs cta" role="img" aria-label="Woman seen from behind looking out over green hills and a valley" style="background:linear-gradient(100deg,#3d4a30 0%,#5f6c45 40%,#8a9168 70%,#6a6548 100%)">
    <h2>Ready to explore more ease<br>and freedom in your body?</h2>
    <p>I'm here to support you.</p>
    <span class="btn-cta">BOOK A SESSION</span>
  </section>

  <!-- newsletter -->
  <section class="abs news">
    <svg class="abs" style="left:62px;top:20px" width="48" height="44" viewBox="0 0 48 44" fill="none" stroke="#fff" stroke-width="1.4"><path d="M6 22L44 4 34 40 22 28z"/><path d="M22 28L44 4"/><path d="M2 14h10M0 22h6M4 30h8"/></svg>
    <h3>STAY CONNECTED</h3>
    <p>Get updates on classes, trainings, workshops and retreats.</p>
    <div class="input">Your email address</div>
    <div class="sub">SUBSCRIBE</div>
    <div class="socials"><i></i><i></i><i></i><i></i></div>
  </section>

  <!-- footer -->
  <footer class="abs footer">
    <div class="f-brand"><span class="brand-dot"></span><span>Liesbet Oonwerk</span></div>
    <p class="f-about">Bodywork. Movement. Education. Different expressions of the same intention.</p>
    <div class="f-col" style="left:293px"><h5>Explore</h5><ul><li>Kavenda</li><li>Movement</li><li>Events</li><li>Work With Me</li></ul></div>
    <div class="f-col" style="left:417px"><h5>About</h5><ul><li>About Me</li><li>Testimonials</li></ul></div>
    <div class="f-col" style="left:532px"><h5>Connect</h5><ul><li>Contact</li><li>Book a Session</li></ul></div>
    <div class="f-col" style="left:660px"><h5>Contact</h5>
      <div class="f-contact"><span class="ico"><svg width="12" height="12" viewBox="0 0 12 12" fill="none" stroke="var(--orange)" stroke-width="1.2"><rect x="1" y="2.5" width="10" height="7"/><path d="M1 3l5 4 5-4"/></svg></span><div><small>Our Email</small>hello@liesbetoonwerk.com</div></div>
      <div class="f-contact"><span class="ico"><svg width="12" height="12" viewBox="0 0 12 12" fill="none" stroke="var(--orange)" stroke-width="1.2"><path d="M3 1l2 3-1 1c1 2 2 3 3 3l1-1 3 2-1 2C5 11 1 7 1 2z"/></svg></span><div><small>Phone Number</small>+31 6 000 482 19</div></div>
    </div>
    <div class="f-quote">“Bodies are<br>plastic to the<br>intent of life.”<small>— Ilse Varen</small></div>
    <div class="f-legal">© Liesbet Oonwerk 2025 &nbsp;|&nbsp; Privacy Policy &nbsp;|&nbsp; Terms &amp; Conditions</div>
  </footer>
</main>
</body>
</html>
```